Restaurant menu design

I need a menu for a restaurant in Spain.
It has to be bohemian but modern. We need something romantic and elegant.
The restaurant is elegant with good food and an excellent reputation. It is also modern at the same time.
The restaurant is superbly decorated and very chick so we need something "class" to fit in with the surroundings.
The size of the document must be 325 mm in high and 245 mm as a maximum and preferably made in indesign.

Reason: Thank you all for your designs.
So far all your designs are ok but it isn´t what we are looking for. Most of the designs are too loaded, too many colors and too much decoration.

Target Market(s)

Adults of various age groups and different nationalities mostly European.

Industry/Entity Type

Restaurant

Requirements
Must have
• The menu must have two interior pages with the text as in the document attached.It must be easily legible.
Nice to have
• See what kind of menus they use in important restaurants in places like Paris, see what designs are in trend, but Not necessarily doing the same style if it doesn’t fit in with the description above.
Should not have
• Nothing old fashioned.

```html
<!DOCTYPE html>
<html lang="es">
<head>
<meta charset="utf-8">
<title>La Soirée — Carta</title>
<link rel="stylesheet" href="https://fonts.googleapis.com/css2?family=Italianno&display=swap">
<style>
  :root {
    --paper: #ffffff;
    --rule: #8a8a8a;
    --ink: #4a4a4a;
    --ink-dark: #2e262d;
    --plum: #8b3f78;
    --ornament-a: #e6e6e6;
    --ornament-b: #f6f6f6;
  }
  * { box-sizing: border-box; margin: 0; padding: 0; }
  html, body { width: 1200px; height: 320px; overflow: hidden; background: var(--paper); }
  .canvas { position: relative; width: 1200px; height: 320px; font-family: "Italianno", cursive; color: var(--ink); }

  .panel { position: absolute; top: 0; height: 320px; border: 1px solid var(--rule); background: var(--paper); }
  .cover { left: 0; width: 160px; }
  .inside-blank { left: 188px; width: 161px; }
  .starters { left: 348px; width: 167px; }
  .fish { left: 533px; width: 160px; }
  .meat { left: 692px; width: 166px; }
  .desserts { left: 878px; width: 160px; }

  .brand { position: absolute; left: 0; right: 0; top: 140px; display: flex; align-items: center; justify-content: center; gap: 6px; }
  .brand-dot { width: 8px; height: 8px; border-radius: 50%; background: var(--plum); }
  .brand-name { font-size: 30px; line-height: 1; color: var(--ink-dark); }

  .section-head { position: absolute; left: 0; right: 0; display: flex; align-items: center; justify-content: center; gap: 3px; }
  .ornament { width: 26px; height: 12px; background: linear-gradient(90deg, var(--ornament-b), var(--ornament-a)); border-radius: 6px; }
  .ornament.right { background: linear-gradient(90deg, var(--ornament-a), var(--ornament-b)); }
  .section-title { font-size: 12px; letter-spacing: 0.3px; color: var(--ink-dark); text-transform: uppercase; white-space: nowrap; }

  .dishes { position: absolute; left: 0; right: 0; list-style: none; text-align: center; font-size: 7.5px; line-height: 11.6px; }
  .dishes .price { margin-left: 4px; }
  .dishes .wrap { display: block; }
  .sauces { position: absolute; left: 30px; right: 30px; top: 291px; display: grid; grid-template-columns: 1fr 1fr; font-size: 7.5px; line-height: 8px; text-align: center; list-style: none; }
</style>
</head>
<body>
<main class="canvas">

  <section class="panel cover">
    <div class="brand">
      <span class="brand-name">la soirée</span>
      <span class="brand-dot"></span>
    </div>
  </section>

  <section class="panel inside-blank"></section>

  <section class="panel starters">
    <header class="section-head" style="top:22px">
      <span class="ornament" role="img" aria-label="Adorno caligráfico de volutas"></span>
      <h2 class="section-title">Entradas</h2>
      <span class="ornament right" role="img" aria-label="Adorno caligráfico de volutas"></span>
    </header>
    <ul class="dishes" style="top:58px">
      <li>Ensalada La Soirée, lechuga, tomate<span class="price">7,50</span></li>
      <li>Ensalada Caprese (Tomate y Mozzarella)<span class="price">7,75</span></li>
      <li>Tomate al Queso de Cabra con Miel<span class="price">8,25</span></li>
      <li>Cocktail de Gambas, Langostinos y Aguacate<span class="price">9,50</span></li>
      <li>La Sopa de Tomate<span class="price">4,90</span></li>
      <li>Crema de Espárragos Trigueros y Calabacín<span class="price">5,50</span></li>
      <li>Carpaccio de Ternera<span class="price">10,50</span></li>
      <li>Carpaccio de Salmón al Eneldo<span class="price">9,75</span></li>
      <li>Carpaccio de Atún<span class="price">10,90</span></li>
      <li>Melón con Jamón Ibérico<span class="price">8,95</span></li>
      <li>Parrillada de Verduras<span class="price">7,50</span></li>
      <li>Parrillada de Verduras Gratinada al<span class="wrap">Queso de Cabra<span class="price">9,50</span></span></li>
    </ul>
  </section>

  <section class="panel fish">
    <header class="section-head" style="top:22px">
      <span class="ornament" role="img" aria-label="Adorno caligráfico de volutas"></span>
      <h2 class="section-title">Pescados Grill</h2>
      <span class="ornament right" role="img" aria-label="Adorno caligráfico de volutas"></span>
    </header>
    <ul class="dishes" style="top:58px; line-height:12.4px">
      <li>Salmón al Horno<span class="price">14,50</span></li>
      <li>Lubina Salvaje a la Sal<span class="wrap">con Berenjenas<span class="price">15,90</span></span></li>
      <li>Filete de Rodaballo en Salsa de Mariscos<span class="price">16,90</span></li>
      <li>Dorada del Mediterráneo<span class="price">15,50</span></li>
      <li>Langosta al Grill con Hierbas Provenzales<span class="price">26,75</span></li>
      <li>Pez Espada a la Plancha con Salsa Verde<span class="price">15,90</span></li>
      <li>Lomo de Salmón con Salsa de Frambuesa<span class="price">15,50</span></li>
      <li>Parrillada de Pescado y Marisco<span class="price">24,50</span></li>
    </ul>
    <header class="section-head" style="top:210px">
      <span class="ornament" role="img" aria-label="Adorno caligráfico de volutas"></span>
      <h2 class="section-title">Especial Niños</h2>
      <span class="ornament right" role="img" aria-label="Adorno caligráfico de volutas"></span>
    </header>
    <ul class="dishes" style="top:246px">
      <li>Solomillo Junior, huevo y patatas fritas<span class="price">8,50</span></li>
      <li>Fish &amp; chips<span class="price">7,50</span></li>
    </ul>
  </section>

  <section class="panel meat">
    <header class="section-head" style="top:22px">
      <span class="ornament" role="img" aria-label="Adorno caligráfico de volutas"></span>
      <h2 class="section-title">Carnes</h2>
      <span class="ornament right" role="img" aria-label="Adorno caligráfico de volutas"></span>
    </header>
    <ul class="dishes" style="top:58px; line-height:11.2px">
      <li>Pechuga de Pollo Rellena con<span class="wrap">Champiñones y Jamón<span class="price">13,50</span></span></li>
      <li>Chuletas de Cordero<span class="price">16,90</span></li>
      <li>Costillas de Cerdo con Salsa Barbacoa<span class="price">13,50</span></li>
      <li>Paletilla de Cordero Lechal<span class="price">18,75</span></li>
      <li>Le Stroganoff: Puntas de Solomillo en su<span class="wrap">Salsa de Champiñones<span class="price">17,90</span></span></li>
      <li>Solomillo de Ternera<span class="price">19,50</span></li>
      <li>Solomillo de Ternera a la Pimienta con Jamón Ibérico y<span class="wrap">Queso, Salsa al Oporto<span class="price">21,50</span></span></li>
      <li>Hamburguesa Gourmet: Picada de Solomillo<span class="wrap">de Ternera, Bacon, Setas y Patatas Fritas<span class="price">14,50</span></span></li>
      <li>Solomillo de Cerdo al Horno con Bacon y su<span class="wrap">Salsa de Setas<span class="price">14,90</span></span></li>
      <li>Entrecot de Ternera<span class="price">16,50</span></li>
      <li>T-Bone Steak de Ternera<span class="price">19,75</span></li>
      <li>Chuletón de Ternera<span class="price">22,50</span></li>
      <li>Parrillada de Carnes y Embutidos<span class="price">21,90</span></li>
    </ul>
    <header class="section-head" style="top:268px">
      <span class="ornament" role="img" aria-label="Adorno caligráfico de volutas"></span>
      <h2 class="section-title">Salsas</h2>
      <span class="ornament right" role="img" aria-label="Adorno caligráfico de volutas"></span>
    </header>
    <ul class="sauces">
      <li>Pimienta<span class="price"> 2,50</span></li>
      <li>Roquefort<span class="price"> 2,50</span></li>
      <li>Bearnesa<span class="price"> 2,50</span></li>
      <li>de Champiñones<span class="price"> 2,50</span></li>
    </ul>
  </section>

  <section class="panel desserts">
    <header class="section-head" style="top:22px">
      <span class="ornament" role="img" aria-label="Adorno caligráfico de volutas"></span>
      <h2 class="section-title">Los Postres de la Soirée</h2>
      <span class="ornament right" role="img" aria-label="Adorno caligráfico de volutas"></span>
    </header>
    <ul class="dishes" style="top:58px; line-height:11.3px">
      <li>Bombones "La Soirée"<span class="price">5,50</span></li>
      <li>Coulant de Chocolate Caliente<span class="price">5,90</span></li>
      <li>Sorbete de Limón, Cava y Vodka<span class="price">5,50</span></li>
      <li>Pastel de Chocolate Casero con su<span class="wrap">Salsa de Vainilla<span class="price">5,90</span></span></li>
      <li>Crème Brûlée<span class="price">5,50</span></li>
      <li>Tarta de Manzana Casera "Tatin" y su<span class="wrap">Helado de Vainilla<span class="price">5,90</span></span></li>
      <li>Copa Helado Doble<span class="price">4,90</span></li>
      <li>Pera al Chocolate Caliente y Helado<span class="wrap">de Frambuesa<span class="price">5,90</span></span></li>
      <li>Tarta de Queso con Coulis de Fresa<span class="price">5,75</span></li>
      <li>Nuestra Mousse de Chocolate<span class="price">5,50</span></li>
    </ul>
  </section>

</main>
</body>
</html>
```